"Trade with Tilly" needs a funky and stylish business card

Hi my name is Tilly, I am an experienced Bidlo Gold Trader with a 100% satisfaction rating and over 400 items sold

My business name and bidlo username is "Trade with Tilly" I sell other peoples items on Bidlo for a commission. The main items I sell are furniture and renovation/building salvage items such as used kitchens, bathrooms , window doors etc.

I will be promoting my service in real estate agent offices, storage facilities, removalists, building and renovating companies.

i believe selling on bidlo is a great way for people to recycle their used goods and salvageable materials and reduce waste and landfill.

Target Market(s)

people selling their homes, renovators, builders, downsizers

Industry/Entity Type

Real Estate

Contact Information for Business Card

Tilly Marchbank
0472906147

Logo Text

Trade with Tilly

Logo styles of interest
Wordmark Logo
Requirements
Must have
• the business card must feature the bidlo logo mentioning goldtraderr top rated seller I have attached a copy
Nice to have
• i would like to have the trade with tilly logo written in royal blue

```html
<!DOCTYPE html>
<html lang="en">
<head>
<meta charset="utf-8">
<title>Trade with Tilly – Business Card</title>
<link href="https://fonts.googleapis.com/css2?family=Gelasio:wght@400&display=swap" rel="stylesheet">
<style>
  :root {
    --card-grey: #b8bec1;
    --card-grey-light: #c6cbce;
    --panel-top: #e3e6ec;
    --panel-bottom: #a7afcd;
    --royal-blue: #1f3ed8;
    --band-blue: #a8b1cc;
    --deep-blue: #2a4fe8;
    --ink: #2e2e2e;
    --seal-gold: #f2b632;
    --mark-navy: #1d2f8a;
  }
  html, body {
    margin: 0;
    padding: 0;
    overflow: hidden;
    background: #ffffff;
  }
  .card {
    position: relative;
    width: 1200px;
    height: 694px;
    overflow: hidden;
    background: radial-gradient(circle at 50% 40%, var(--card-grey-light), var(--card-grey));
    font-family: "Gelasio", Georgia, serif;
    color: var(--ink);
  }
  .card-art {
    position: absolute;
    inset: 0;
    width: 1200px;
    height: 694px;
  }
  .contact {
    position: absolute;
    top: 52px;
    right: 38px;
    text-align: right;
    font-variant-numeric: oldstyle-nums;
  }
  .contact-name {
    margin: 0;
    font-size: 46px;
    font-weight: 400;
    letter-spacing: 1.5px;
    line-height: 1.1;
  }
  .contact-phone {
    margin: 22px 0 0;
    font-size: 46px;
    letter-spacing: 2px;
    line-height: 1.1;
  }
  .wordmark {
    font-family: "Gelasio", Georgia, serif;
    fill: var(--royal-blue);
    font-size: 46px;
  }
  .partner-mark {
    font-family: "Gelasio", Georgia, serif;
    fill: var(--mark-navy);
    font-weight: 400;
  }
</style>
</head>
<body>
<main class="card">
  <svg class="card-art" viewBox="0 0 1061 614" preserveAspectRatio="none">
    <defs>
      <linearGradient id="side-panel" x1="0" y1="0" x2="0.3" y2="1">
        <stop offset="0" stop-color="var(--panel-top)"/>
        <stop offset="1" stop-color="var(--panel-bottom)"/>
      </linearGradient>
    </defs>

    <!-- left side panel bounded by the curve -->
    <path class="side-panel" fill="url(#side-panel)"
          d="M0,0 L243,0 C180,60 110,120 92,170 C78,205 110,214 180,220 C215,225 222,260 200,295 L55,614 L0,614 Z"/>

    <!-- highlight under the curve -->
    <path class="curve-highlight" fill="none" stroke="#ffffff" stroke-width="12" stroke-linecap="round"
          d="M86,185 C78,222 120,230 175,236 C198,240 204,262 196,282"/>

    <!-- royal blue curve -->
    <path class="side-curve" fill="none" stroke="var(--royal-blue)" stroke-width="12" stroke-linejoin="round"
          d="M243,0 C180,60 110,120 92,170 C78,205 110,214 180,220 C215,225 222,260 200,295 L55,614"/>

    <!-- business wordmark running along the curve -->
    <text class="wordmark" transform="translate(230 346) rotate(-57)"
          textLength="360" lengthAdjust="spacingAndGlyphs">Trade with Tilly</text>

    <!-- bottom-right sweeps -->
    <path class="sweep-light" fill="var(--band-blue)"
          d="M1061,228 C920,410 760,560 560,614 L1061,614 Z"/>
    <path class="sweep-blue" fill="var(--deep-blue)"
          d="M1061,330 C960,480 830,580 690,614 L1061,614 Z"/>

    <!-- top-rated seller seal -->
    <circle class="seller-seal" cx="123" cy="466" r="46" fill="var(--seal-gold)"/>

    <!-- partner mark -->
    <text class="partner-mark" x="150" y="578" font-size="64">Bidlo</text>
    <text class="partner-mark" x="268" y="606" font-size="19">Gold Trader</text>
  </svg>

  <section class="contact">
    <h1 class="contact-name">Tilly Marchbank</h1>
    <p class="contact-phone">0472906147</p>
  </section>
</main>
</body>
</html>
```